Kettle Ledger Business Card design

We need a stand out business card design for Accounting practice based in Australia specialising in pubs, clubs and hotels. We help venues maximise margins, create time and manage cashflow. One club we have been working with for the last 6 months has increased revenue by 3% and margin by 5% in this time frame. We have a back office outsourced system that costs less than having a full time employee and also allows the venues the added benefit of:<br/>-using the office space to become a revenue generating opportunity. <br/>-a complete system to enhance governance, accountability and efficiency within their operation<br/>-52 weeks cover so no hassle to cover annual/sick .. leave<br/><br/>We would like to see designs that use the colours of our logo (green & blue).
Target Market(s)
Australian Pubs, Clubs & Hotels abookkeeping, accounting and tax services
Industry/Entity Type
Accountant
Contact Information for Business Card
Miriam Oakley CPA
Principal
Accountant Tax Agent
Miriam@KettleLedger-example.com.au
0418693142
www.kettleledger-example.com.au
Accounting / Payroll / Tax / SMSF / Technology
Colors
Designer to choose colors to be used in the design.
Look and feel
Each slider illustrates characteristics of the customer's brand and the style your logo design should communicate.

```html
<!DOCTYPE html>
<html lang="en">
<head>
<meta charset="utf-8">
<title>Kettle Ledger Business Card</title>
<link href="https://fonts.googleapis.com/css2?family=Montserrat:wght@800&family=Lato:wght@400;700&display=swap" rel="stylesheet">
<style>
  :root {
    --backdrop: #2f2f2f;
    --brand-green: #08703d;
    --brand-blue: #1f3f99;
    --ink: #333333;
    --rule: #c9c9c9;
    --paper: #ffffff;
  }
  * { box-sizing: border-box; margin: 0; padding: 0; }
  html, body {
    width: 1200px; height: 866px; overflow: hidden;
    background: var(--backdrop);
  }
  .sheet {
    width: 1200px; height: 866px;
    display: flex; flex-direction: column; align-items: center; justify-content: center;
    gap: 40px;
  }
  .card {
    width: 620px; height: 379px; position: relative; overflow: hidden;
    box-shadow: 0 8px 22px rgba(0,0,0,.45);
  }

  /* Front */
  .card-front { background: var(--paper); border-bottom: 12px solid var(--brand-green); }
  .contact {
    position: absolute; left: 44px; top: 70px;
    font-family: "Lato", sans-serif; color: var(--ink);
  }
  .contact-name {
    font-family: "Montserrat", sans-serif; font-weight: 800;
    font-size: 19px; color: var(--brand-blue); letter-spacing: .5px;
    text-transform: uppercase;
  }
  .contact-name .credential { color: var(--brand-green); }
  .contact-role { font-size: 16px; line-height: 1.25; margin-top: 4px; }
  .contact-lines { list-style: none; margin-top: 12px; font-size: 16px; line-height: 1.45; }
  .contact-lines li { display: flex; align-items: center; gap: 7px; }
  .contact-lines svg { width: 16px; height: 16px; flex: none; }
  .contact-lines .web { color: var(--brand-blue); }
  .name-rule {
    position: absolute; left: 290px; right: 40px; top: 104px;
    border-top: 1px solid var(--rule);
  }
  .wordmark {
    position: absolute; right: 40px; top: 262px;
    display: flex; align-items: center; gap: 14px;
  }
  .wordmark-dot { width: 46px; height: 46px; border-radius: 50%; background: var(--brand-green); }
  .wordmark-name {
    font-family: "Montserrat", sans-serif; font-weight: 800;
    font-size: 38px; color: var(--brand-blue); letter-spacing: -.5px;
    white-space: nowrap;
  }

  /* Back */
  .card-back {
    background: var(--brand-green);
    display: flex; flex-direction: column; align-items: center; justify-content: center;
    gap: 22px; color: var(--paper);
  }
  .card-back .wordmark-name { color: var(--paper); font-size: 54px; }
  .services {
    font-family: "Lato", sans-serif; font-size: 15px; letter-spacing: 1px;
    text-transform: uppercase;
  }
</style>
</head>
<body>
<main class="sheet">
  <section class="card card-front">
    <div class="contact">
      <h1 class="contact-name">Miriam Oakley <span class="credential">CPA</span></h1>
      <p class="contact-role">Principal<br>Accountant Tax Agent</p>
      <ul class="contact-lines">
        <li>
          <svg viewBox="0 0 16 16" aria-hidden="true"><rect x="1" y="1" width="14" height="14" rx="2" fill="none" stroke="#1f3f99" stroke-width="1.5"/><path d="M5 4c0 4 3 7 7 7l0-2-2-.5-1 1c-1.3-.6-2.3-1.6-2.9-2.9l1-1L6.6 4z" fill="#1f3f99"/></svg>
          0418693142
        </li>
        <li>
          <svg viewBox="0 0 16 16" aria-hidden="true"><rect x="1" y="3" width="14" height="10" fill="#1f3f99"/><path d="M1 3l7 6 7-6" fill="none" stroke="#fff" stroke-width="1.2"/></svg>
          Miriam@KettleLedger-example.com.au
        </li>
        <li class="web">
          <svg viewBox="0 0 16 16" aria-hidden="true"><circle cx="8" cy="8" r="7" fill="#1f3f99"/><path d="M1 8h14M8 1c-3 4-3 10 0 14M8 1c3 4 3 10 0 14M2.5 4.5h11M2.5 11.5h11" fill="none" stroke="#fff" stroke-width=".9"/></svg>
          www.kettleledger-example.com.au
        </li>
      </ul>
    </div>
    <div class="name-rule"></div>
    <div class="wordmark">
      <span class="wordmark-dot"></span>
      <span class="wordmark-name">Kettle Ledger</span>
    </div>
  </section>

  <section class="card card-back">
    <span class="wordmark-name">Kettle Ledger</span>
    <p class="services">Accounting / Payroll / Tax / SMSF / Technology</p>
  </section>
</main>
</body>
</html>
```